Cellular Repair Retail Store Flyer/Postcards

We are looking for a good flyer for us to print and distribute as well as post on various web sites. Our company name is "Handset Fixit Crew" and we repair a wide range of cellular phones from Zelphones to Zelpads, Varnok's,,QT's, Brivanta, and PWD. In general if you have a cell phone we repair it. Cellular repairs is the primary focus however we are also an accessory superstore with 1'000's of choices of phone cases for all model phones. Historically these phone cases have all been aftermarket however now there are a number of brands. I'll attach a few so we have the ability to use some branded logo's on the flyer. Not all the graphics need to be used that we are providing. Again the flyer's main objective is, 1) Cellular Repairs, 2) Our location & pic of building (I have one attached but i'll have a new one within 24 hours and 3) Cellular Accessory Superstore with 1,000's of case. The address to our location is 4817 N 19th Street, Milwaukee, Wisconsin 53209. Anytime we use our address we state "2 Blocks North of 19th & Pemberly" (popular intersection in the market). So i'm not sure what approach to go... but I figured i'd provide a bunch of stuff for you to pick from. Naturally let's not make the flyer too busy but if we hit the 3 main deal points we will be good. Attached are; some pics of attractive phone cases, a few cellular accessory brands such as Heron Shell, Valdoro, Skinmitten, LuVenn, Cragmore etc. These logo's may add a nice appeal given they are national companies. For your reference and to be listed on the flyer is our web site; www.handsetfixitcrew.example

Requirements
Must have
• This advertisement will be used for the Postal Porchdrop Bulk Mailer so we need to make the flyer with the following measurements in mind; 6.25" x 9"
Nice to have
• In addition to repairing phones we need to promote we buy used and broken smart phones. Repairs done on site with certified technicians.

```html
<!DOCTYPE html>
<html lang="en">
<head>
<meta charset="utf-8">
<title>Handset Fixit Crew – Fix Your Phone Today</title>
<link rel="stylesheet" href="https://fonts.googleapis.com/css2?family=Montserrat:wght@300;400;700;900&family=Didact+Gothic&display=swap">
<style>
  :root {
    --white: #ffffff;
    --sky: #1b9cf0;
    --ink: #2b3845;
    --navy: #1f3a52;
    --mustard: #f2c744;
    --gold: #e6a817;
    --frame: #dbe9f6;
    --photo-sky: #6fa8dc;
    --photo-ground: #b9b3a8;
    --phone-dark: #1d1d1f;
    --phone-screen: #6fb3e6;
  }
  * { box-sizing: border-box; margin: 0; padding: 0; }
  html, body { width: 837px; height: 1200px; overflow: hidden; background: var(--white); }
  .flyer {
    position: relative; width: 837px; height: 1200px; overflow: hidden;
    font-family: "Didact Gothic", "Montserrat", sans-serif; color: var(--ink);
    background: var(--white);
  }
  .band { position: absolute; left: 0; width: 100%; }
  .band--hero { top: 290px; height: 386px; background: var(--sky); }
  .band--services { top: 680px; height: 261px; background: var(--mustard); }
  .band--location { top: 941px; height: 259px; background: var(--navy); }

  .brand { position: absolute; left: 460px; top: 40px; width: 370px; text-align: center; }
  .brand__name {
    font-family: "Montserrat", sans-serif; font-weight: 700; font-size: 35px;
    color: var(--navy); letter-spacing: -0.5px; line-height: 1;
  }
  .brand__url { margin-top: 44px; font-size: 19px; color: var(--ink); line-height: 1; }

  .hero-art {
    position: absolute; left: 53px; top: 118px; width: 353px; height: 433px;
    border-radius: 40px;
    background: linear-gradient(135deg, var(--phone-dark) 0%, #3d3f44 35%, var(--phone-screen) 60%, #a9adb3 100%);
  }

  .headline {
    position: absolute; left: 396px; top: 236px;
    font-family: "Montserrat", sans-serif; color: var(--ink); line-height: 1;
  }
  .headline__fix {
    font-weight: 900; font-size: 120px; letter-spacing: -2px;
    -webkit-text-stroke: 5px var(--white); paint-order: stroke fill;
  }
  .headline__line { font-weight: 400; font-size: 94px; letter-spacing: -4px; margin-top: -2px; }
  .headline__line--today { color: var(--white); font-weight: 300; font-size: 86px; letter-spacing: -3px; margin-top: 8px; }

  .call-badge {
    position: absolute; left: 89px; top: 570px; width: 267px; height: 61px;
    background: var(--gold); display: flex; align-items: center; gap: 10px;
    padding-left: 16px; font-size: 27px; color: var(--ink);
  }
  .call-badge svg { width: 30px; height: 30px; }

  .services { position: absolute; left: 86px; top: 703px; list-style: none; }
  .services li {
    position: relative; padding-left: 28px; font-size: 21px; line-height: 38px; color: var(--ink);
    white-space: nowrap;
  }
  .services li::before {
    content: ""; position: absolute; left: 0; top: 15px; width: 9px; height: 9px;
    border-radius: 50%; background: var(--ink);
  }

  .photo { position: absolute; border: 5px solid var(--white); }
  .photo--interior {
    left: 583px; top: 700px; width: 213px; height: 206px;
    background: linear-gradient(180deg, #e8ecf0 0%, #b7c3d8 45%, #c78a6a 100%);
  }
  .photo--storefront {
    left: 40px; top: 905px; width: 348px; height: 228px; border: 9px solid var(--frame);
    background: linear-gradient(180deg, var(--photo-sky) 0%, #a9cbe8 40%, #e8e2d8 55%, var(--photo-ground) 100%);
  }

  .address { position: absolute; left: 440px; top: 975px; color: var(--white); font-style: normal; }
  .address__landmark { font-size: 28px; line-height: 38px; padding-left: 3px; }
  .address__street { margin-top: 10px; font-size: 21px; line-height: 38px; }
</style>
</head>
<body>
<main class="flyer">
  <div class="band band--hero"></div>
  <div class="band band--services"></div>
  <div class="band band--location"></div>

  <header class="brand">
    <div class="brand__name">Handset Fixit Crew</div>
    <div class="brand__url">www.handsetfixitcrew.example</div>
  </header>

  <div class="hero-art" role="img" aria-label="Illustration of a smartphone with a wrench laid across its screen"></div>

  <h1 class="headline">
    <div class="headline__fix">FIX</div>
    <div class="headline__line">YOUR</div>
    <div class="headline__line">PHONE</div>
    <div class="headline__line headline__line--today">TODAY</div>
  </h1>

  <div class="call-badge">
    <svg viewBox="0 0 24 24" aria-hidden="true"><path fill="#2b3845" d="M6.6 10.8a15.1 15.1 0 0 0 6.6 6.6l2.2-2.2a1 1 0 0 1 1-.25 11.4 11.4 0 0 0 3.6.57 1 1 0 0 1 1 1V20a1 1 0 0 1-1 1A17 17 0 0 1 3 4a1 1 0 0 1 1-1h3.5a1 1 0 0 1 1 1c0 1.25.2 2.45.57 3.57a1 1 0 0 1-.25 1z"/></svg>
    <span>414-555-0172</span>
  </div>

  <ul class="services">
    <li>Water Damage</li>
    <li>Broken glass and LCDs</li>
    <li>Battery replacement and charging port</li>
    <li>Camera and home button replacement</li>
    <li>Accessory superstore: 1,000's of cases</li>
  </ul>

  <div class="photo photo--interior" role="img" aria-label="Photo of the store interior with walls of phone cases and accessory displays"></div>
  <div class="photo photo--storefront" role="img" aria-label="Photo of the storefront building with black awnings under a blue sky"></div>

  <address class="address">
    <div class="address__landmark">2 Blocks North of<br>19th &amp; Pemberly</div>
    <div class="address__street">4817 N 19th Street,<br>Milwaukee, Wisconsin 53209</div>
  </address>
</main>
</body>
</html>
```